Flyer in Creole

Instructions for Designer
Objective: Create two versions of the flyer for Densora dental services: one in French and one in Creole. Target audience is elders of the haitian community in Montreal so include picture of an older person with a darker skin complexion.

I have included our original flyer.

Densora - Sèvis Dantè pou Granmoun Aje
Nou ofri swen dantè san frè pou moun 65 an e plis!

La Clinique Dentaire Densora gen kè kontan patisipe nan Pwogram Sourir Nasyonal (PSNB). Si w gen 65 an oubyen plis, ou ka resevwa swen dantè gratis, san frè siplemantè si w kalifye.

Kijan pou Kalifye?

Si w gen 65 an ou plis, ou ka jwenn tretman dantè san frè.
Vizite: https://www.plansourir-exemple.org/aplike/fomile.html pou w aplike epi w konnen si w kalifye.
Sèvis Nou Ofri:

Netwayaj dantè: Sante bouch ou enpòtan, fè yon netwayaj pwofesyonèl pou prezève sante dantè w.
Egzamen ak radyografi: Pran yon randevou pou yon egzamen konplè ak radyografi.
Ekstraksyon dantè: Retire dan ki domaje oswa ki fè w mal.
Ijans dantè: Tretman rapid pou doulè, dan kase, oswa lòt ijans.
Pwotèz dantè konplè ak pasyèl: Nou ranplase dan ki manke yo pou yon bèl souri ak bon sante.
Rele Kounye a pou Fiks yon Randevou: 514-555-0187
Klinik Densora - 2860 Rue Belmarais E, 2yèm etaj, Montreal, QC H2X 3K9
Design Elements:
Use images that resonate with the Creole-speaking community.
Ensure the text is clear and accessible.

```html
<!DOCTYPE html>
<html lang="fr">
<head>
<meta charset="utf-8">
<title>Densora – Flyers français et créole</title>
<link rel="stylesheet" href="https://fonts.googleapis.com/css2?family=Montserrat:ital,wght@0,400;0,600;0,700;0,800;1,400;1,600;1,700;1,800&family=Open+Sans:ital,wght@0,400;0,600;1,400&display=swap">
<style>
:root{
  --navy:#22334f;
  --sky:#c5dbf5;
  --sky-deep:#9fbfe6;
  --paper:#ffffff;
  --mist:#eceef2;
  --grey-text:#5d6470;
  --skin-dark:#5a3426;
  --skin-mid:#8a5a42;
  --photo-bg:#cfc9c6;
}
*{margin:0;padding:0;box-sizing:border-box}
html,body{width:1200px;height:776px;overflow:hidden;background:var(--paper)}
body{position:relative;font-family:"Open Sans",Arial,sans-serif;color:var(--navy)}
.flyer{position:absolute;top:80px;width:440px;height:620px;overflow:hidden;box-shadow:0 4px 14px rgba(0,0,0,.28)}
.flyer-fr{left:101px;background:var(--paper)}
.flyer-ht{left:665px;background:var(--mist)}
.abs{position:absolute}
.brand{font-family:"Montserrat",Arial,sans-serif;font-weight:700;color:var(--navy);letter-spacing:-1px;line-height:1}
.shape{position:absolute}
.photo{position:absolute}

/* ---------- French flyer ---------- */
.fr-logo{left:34px;top:44px;font-size:36px}
.fr-title{left:34px;top:94px;width:180px;font-family:"Montserrat",sans-serif;font-weight:800;font-size:11.4px;line-height:13.5px;text-transform:uppercase}
.fr-tagline{left:34px;top:122px;width:180px;font-family:"Montserrat",sans-serif;font-weight:700;font-style:italic;font-size:7.8px;line-height:12px}
.fr-intro{left:34px;top:163px;width:178px;font-size:8.4px;line-height:13.3px;color:var(--navy)}
.fr-hero{left:222px;top:0;width:218px;height:247px;background:radial-gradient(ellipse at 55% 55%,var(--skin-mid) 0%,var(--skin-dark) 38%,#8f8a8c 62%,var(--photo-bg) 100%)}
.fr-accent-strip{left:0;top:185px;width:16px;height:55px;background:var(--sky);clip-path:polygon(0 30%,100% 0,100% 80%,0 100%)}
.fr-services{left:0;top:247px;width:440px;height:160px;background:var(--navy)}
.fr-services-title{left:0;top:16px;width:440px;text-align:center;font-family:"Montserrat",sans-serif;font-weight:700;font-size:15px;color:#fff}
.service-card{position:absolute;top:67px;width:77px;height:81px;border:1px solid rgba(255,255,255,.18);border-radius:4px;background:rgba(255,255,255,.06);text-align:center;padding:24px 3px 0}
.service-card h3{font-family:"Montserrat",sans-serif;font-weight:700;font-size:6.6px;line-height:8.6px;color:#fff}
.service-card p{font-size:5.3px;line-height:8px;color:#c9d2de;margin-top:2px}
.hex{position:absolute;top:-20px;left:50%;margin-left:-18px;width:36px;height:40px}
.fr-smile{left:0;top:407px;width:188px;height:179px;background:linear-gradient(135deg,var(--skin-mid) 0%,var(--skin-dark) 45%,#e9e2dc 75%,#b7a69b 100%)}
.fr-qualify{left:208px;top:420px;width:215px}
.fr-qualify h2{font-family:"Montserrat",sans-serif;font-weight:700;font-size:13.5px;color:#101a2a}
.fr-qualify p{font-size:7.3px;line-height:10.4px;color:var(--grey-text);margin-top:9px}
.fr-call{left:208px;top:513px;font-family:"Montserrat",sans-serif;font-weight:700;font-size:8.6px;color:#101a2a}
.fr-phone{left:208px;top:529px;width:92px;height:22px;background:var(--navy);border-radius:3px;color:#fff;font-family:"Montserrat",sans-serif;font-weight:700;font-size:8px;display:flex;align-items:center;gap:5px;padding-left:6px}
.fr-address{left:217px;top:561px;display:flex;gap:6px;font-size:7.8px;line-height:10px;color:#101a2a}
.fr-footer{left:0;top:586px;width:440px;height:34px;background:var(--navy)}
.fr-slogan{right:20px;top:8px;font-family:"Montserrat",sans-serif;font-weight:700;font-style:italic;font-size:11.4px;color:#fff}

/* ---------- Creole flyer ---------- */
.ht-header{left:0;top:0;width:440px;height:67px;background:#eef0f3}
.ht-logo{left:25px;top:17px;font-size:38px}
.ht-rule{left:210px;top:39px;width:230px;height:1.5px;background:var(--navy)}
.ht-dot{top:35px;width:10px;height:10px;border-radius:50%;background:var(--navy)}
.ht-hero{left:0;top:67px;width:440px;height:172px;background:radial-gradient(ellipse at 40% 45%,var(--skin-mid) 0%,var(--skin-dark) 35%,#7e6f69 60%,var(--photo-bg) 100%)}
.ht-hero-title{left:15px;top:196px;font-family:"Montserrat",sans-serif;font-weight:800;font-style:italic;font-size:16.5px;line-height:21px;color:#fff;text-transform:uppercase}
.ht-intro{right:25px;top:166px;width:128px;text-align:right;font-style:italic;font-size:7.6px;line-height:10.6px;color:var(--navy)}
.ht-offer{left:23px;top:254px;width:118px;font-family:"Montserrat",sans-serif;font-weight:800;font-style:italic;font-size:13.2px;line-height:15px;color:var(--navy);text-transform:uppercase}
.ht-offer-title{right:25px;top:253px;font-family:"Montserrat",sans-serif;font-weight:800;font-style:italic;font-size:21px;letter-spacing:-1px;color:#fff;text-transform:uppercase}
.ht-h{font-family:"Montserrat",sans-serif;font-weight:800;font-size:11px;letter-spacing:-.5px;line-height:12.5px;color:var(--navy);text-transform:uppercase}
.ht-qualify{left:15px;top:361px;width:175px}
.ht-qualify p{font-size:8.1px;line-height:12.2px;margin:8px 0 0 10px;color:#1b2433;word-break:break-all}
.ht-call{left:15px;top:470px;width:165px}
.ht-contact{left:25px;display:flex;align-items:center;gap:9px}
.icon-circle{width:28px;height:28px;border-radius:50%;background:var(--navy);display:flex;align-items:center;justify-content:center;flex-shrink:0}
.ht-phone-num{font-family:"Montserrat",sans-serif;font-style:italic;font-size:12px;color:var(--navy)}
.ht-address{font-family:"Montserrat",sans-serif;font-style:italic;font-size:7.8px;line-height:12px;color:var(--navy)}
.ht-service{left:213px;width:205px;display:flex;gap:9px;align-items:flex-start}
.ht-service .icon-circle{width:34px;height:34px}
.ht-service h3{font-family:"Montserrat",sans-serif;font-weight:700;font-size:7.2px;line-height:8px;color:var(--navy);text-transform:uppercase;margin-top:3px}
.ht-service p{font-style:italic;font-size:6.8px;line-height:9.8px;color:#1b2433;margin-top:5px;text-align:justify}
.ht-slogan{right:24px;top:597px;font-family:"Montserrat",sans-serif;font-weight:700;font-style:italic;font-size:8px;color:var(--navy)}
</style>
</head>
<body>

<svg width="0" height="0" style="position:absolute" aria-hidden="true">
  <defs>
    <symbol id="tooth" viewBox="0 0 24 24">
      <path d="M7 3c-3 0-4.5 2.5-4 5.5.4 2.3 1.6 3.6 2 6 .4 2.6.8 6.5 2.6 6.5 1.7 0 1.6-4.6 4.4-4.6s2.7 4.6 4.4 4.6c1.8 0 2.2-3.9 2.6-6.5.4-2.4 1.6-3.7 2-6 .5-3-1-5.5-4-5.5-2 0-3 1-5 1S9 3 7 3z" fill="none" stroke="currentColor" stroke-width="1.5" stroke-linejoin="round"/>
    </symbol>
    <symbol id="phone" viewBox="0 0 24 24">
      <path d="M6.6 10.8a15 15 0 0 0 6.6 6.6l2.2-2.2c.3-.3.7-.4 1-.2 1.1.4 2.3.6 3.6.6.6 0 1 .4 1 1V20c0 .6-.4 1-1 1A17 17 0 0 1 3 4c0-.6.4-1 1-1h3.5c.6 0 1 .4 1 1 0 1.3.2 2.5.6 3.6.1.3 0 .7-.2 1l-2.3 2.2z" fill="currentColor"/>
    </symbol>
    <symbol id="pin" viewBox="0 0 24 24">
      <path d="M12 2a7 7 0 0 0-7 7c0 5.2 7 13 7 13s7-7.8 7-13a7 7 0 0 0-7-7zm0 9.5A2.5 2.5 0 1 1 12 6.5a2.5 2.5 0 0 1 0 5z" fill="currentColor"/>
    </symbol>
    <symbol id="hexagon" viewBox="0 0 36 40">
      <path d="M18 1l16 9v20l-16 9-16-9V10z" fill="#d6e5f7"/>
    </symbol>
  </defs>
</svg>

<!-- ================= French flyer ================= -->
<section class="flyer flyer-fr" lang="fr">
  <div class="photo fr-hero" role="img" aria-label="Photo d'une femme âgée à la peau foncée, souriante, lors d'un soin dentaire"></div>
  <svg class="shape" style="left:0;top:0" width="440" height="247" aria-hidden="true">
    <polygon points="206,0 343,0 206,75" fill="var(--navy)"/>
    <polygon points="440,182 440,247 320,247" fill="var(--paper)"/>
  </svg>
  <div class="shape fr-accent-strip"></div>

  <div class="abs brand fr-logo">Densora</div>
  <h1 class="abs fr-title">Services dentaires pour les personnes âgées</h1>
  <p class="abs fr-tagline">Nous offrons des soins dentaires gratuits pour les personnes de 65 ans et plus!</p>
  <p class="abs fr-intro">La Clinique Dentaire Densora est heureuse de participer au Programme Sourire National (PSNB). Si vous avez 65 ans ou plus, vous pouvez recevoir des soins dentaires gratuitement, sans frais supplémentaires si vous êtes admissible.</p>

  <div class="abs fr-services">
    <h2 class="abs fr-services-title">Services que Nous Offrons</h2>
    <div class="service-card" style="left:18px"><svg class="hex"><use href="#hexagon"/></svg><svg class="abs" style="left:29px;top:-12px;color:var(--navy)" width="19" height="19"><use href="#tooth"/></svg><h3>Nettoyage dentaire</h3><p>La santé de votre bouche est importante. Recevez un nettoyage professionnel pour maintenir votre santé dentaire.</p></div>
    <div class="service-card" style="left:99px"><svg class="hex"><use href="#hexagon"/></svg><svg class="abs" style="left:29px;top:-12px;color:var(--navy)" width="19" height="19"><use href="#tooth"/></svg><h3>Examens et radiographies</h3><p>Prenez rendez-vous pour un examen complet et des radiographies.</p></div>
    <div class="service-card" style="left:180px"><svg class="hex"><use href="#hexagon"/></svg><svg class="abs" style="left:29px;top:-12px;color:var(--navy)" width="19" height="19"><use href="#tooth"/></svg><h3>Extractions dentaires</h3><p>Enlevez les dents endommagées ou douloureuses.</p></div>
    <div class="service-card" style="left:261px"><svg class="hex"><use href="#hexagon"/></svg><svg class="abs" style="left:29px;top:-12px;color:var(--navy)" width="19" height="19"><use href="#tooth"/></svg><h3>Urgences dentaires</h3><p>Traitement rapide pour douleurs, dents cassées, ou autres urgences.</p></div>
    <div class="service-card" style="left:345px"><svg class="hex"><use href="#hexagon"/></svg><svg class="abs" style="left:29px;top:-12px;color:var(--navy)" width="19" height="19"><use href="#tooth"/></svg><h3>Prothèses complètes et partielles</h3><p>Remplacement des dents manquantes pour un sourire éclatant et une bonne santé.</p></div>
  </div>

  <div class="photo fr-smile" role="img" aria-label="Gros plan d'un sourire de personne âgée pendant un examen dentaire"></div>
  <svg class="shape" style="left:0;top:407px" width="200" height="179" aria-hidden="true">
    <polygon points="118,179 198,135 198,179" fill="var(--navy)"/>
  </svg>

  <div class="abs fr-qualify">
    <h2>Comment se Qualifier?</h2>
    <p>Si vous avez 65 ans ou plus, vous pouvez recevoir des soins dentaires gratuits.<br>Visitez:<br>https://www.plansourir-exemple.org/fr/demande.html pour postuler et vérifier votre admissibilité.</p>
  </div>
  <p class="abs fr-call">Appelez Maintenant pour Prendre Rendez-vous</p>
  <div class="abs fr-phone"><span style="width:14px;height:14px;border-radius:3px;background:var(--sky);display:flex;align-items:center;justify-content:center;color:var(--navy)"><svg width="9" height="9"><use href="#phone"/></svg></span>514-555-0187</div>
  <div class="abs fr-address"><svg width="10" height="12" style="color:var(--navy);margin-top:4px"><use href="#pin"/></svg><span>Clinique Densora - 2860 Rue Belmarais<br>Est, 2ème étage, Montréal, QC H2X 3K9</span></div>

  <div class="abs fr-footer"><p class="abs fr-slogan">Gardez votre sourire en bonne santé!</p></div>
</section>

<!-- ================= Creole flyer ================= -->
<section class="flyer flyer-ht" lang="ht">
  <div class="abs ht-header"></div>
  <svg class="shape" style="left:0;top:0" width="440" height="14" aria-hidden="true">
    <polygon points="343,13 358,0 440,0 440,13" fill="var(--navy)"/>
  </svg>
  <div class="abs brand ht-logo">Densora</div>
  <div class="abs ht-rule"></div>
  <div class="abs ht-dot" style="left:373px"></div>
  <div class="abs ht-dot" style="left:389px"></div>
  <div class="abs ht-dot" style="left:405px"></div>

  <div class="photo ht-hero" role="img" aria-label="Photo en gros plan d'une femme âgée à la peau foncée, au large sourire"></div>

  <svg class="shape" style="left:0;top:0" width="440" height="360" aria-hidden="true">
    <polygon points="308,161 349,122 440,122 440,161" fill="var(--navy)"/>
    <line x1="318" y1="161" x2="352" y2="130" stroke="#fff" stroke-width=".8"/>
    <polygon points="212,236 291,161 440,161 440,236" fill="var(--sky)"/>
    <polygon points="0,239 250,239 190,343 0,343" fill="var(--sky)"/>
    <polygon points="166,296 227,236 440,236 440,296" fill="var(--navy)"/>
    <line x1="193" y1="283" x2="242" y2="236" stroke="#fff" stroke-width=".8"/>
    <line x1="147" y1="353" x2="208" y2="296" stroke="var(--navy)" stroke-width=".8"/>
    <line x1="232" y1="320" x2="415" y2="320" stroke="var(--sky-deep)" stroke-width="1"/>
  </svg>

  <p class="abs ht-intro">Klinik Densora gen kè kontan patisipe nan Pwogram Sourir Nasyonal (PSNB). Si w gen 65 an oubyen plis, ou ka resevwa swen dantè gratis, san frè siplemantè si w kalifye.</p>
  <h1 class="abs ht-hero-title">Sèvis Dantè pou<br>Granmoun Aje</h1>
  <p class="abs ht-offer">Nou ofri swen dantè san frè pou moun 65 an e plis!</p>
  <h2 class="abs ht-offer-title">Sèvis nou ofri:</h2>

  <div class="abs ht-qualify">
    <h2 class="ht-h">Kijan pou kalifye?</h2>
    <p>Si w gen 65 an ou plis, ou ka jwenn tretman dantè san frè.<br>Vizite:<br>https://www.plansourir-exemple.org/aplike/fomile.html pou w aplike epi w konnen si w kalifye.</p>
  </div>

  <h2 class="abs ht-h ht-call">Rele kounye a pou fiks yon randevou</h2>
  <div class="abs ht-contact" style="top:499px"><span class="icon-circle"><svg width="14" height="14" style="color:#fff"><use href="#phone"/></svg></span><span class="ht-phone-num">514-555-0187</span></div>
  <div class="abs ht-contact" style="top:534px;left:23px"><span class="icon-circle"><svg width="13" height="13" style="color:#fff"><use href="#pin"/></svg></span><span class="ht-address">2860 Rue Belmarais E, 2yèm<br>etaj, Montreal, QC H2X 3K9</span></div>

  <div class="abs ht-service" style="top:345px"><span class="icon-circle"><svg width="18" height="18" style="color:#fff"><use href="#tooth"/></svg></span><div><h3>Netwayaj dantè</h3><p>Sante bouch ou enpòtan, fè yon netwayaj pwofesyonèl pou prezève sante dantè w.</p></div></div>
  <div class="abs ht-service" style="top:384px"><span class="icon-circle"><svg width="18" height="18" style="color:#fff"><use href="#tooth"/></svg></span><div><h3>Egzamen ak radyografi</h3><p>Pran yon randevou pou yon egzamen konplè ak radyografi.</p></div></div>
  <div class="abs ht-service" style="top:426px"><span class="icon-circle"><svg width="18" height="18" style="color:#fff"><use href="#tooth"/></svg></span><div><h3>Ekstraksyon dantè</h3><p>Retire dan ki domaje oswa ki fè w mal.</p></div></div>
  <div class="abs ht-service" style="top:468px"><span class="icon-circle"><svg width="18" height="18" style="color:#fff"><use href="#tooth"/></svg></span><div><h3>Ijans dantè</h3><p>Tretman rapid pou doulè, dan kase, oswa lòt ijans.</p></div></div>
  <div class="abs ht-service" style="top:509px"><span class="icon-circle"><svg width="18" height="18" style="color:#fff"><use href="#tooth"/></svg></span><div><h3>Pwotèz dantè konplè ak pasyèl</h3><p>Nou ranplase dan ki manke yo pou yon bèl souri ak bon sante.</p></div></div>

  <svg class="shape" style="left:0;top:575px" width="440" height="45" aria-hidden="true">
    <polygon points="0,3 219,3 191,29 0,29" fill="var(--navy)"/>
    <line x1="205" y1="16" x2="415" y2="16" stroke="var(--navy)" stroke-width="1"/>
    <line x1="199" y1="29" x2="258" y2="29" stroke="var(--navy)" stroke-width=".8"/>
  </svg>
  <p class="abs ht-slogan">KENBE SOURI W AN SANTE AK BÈL!</p>
</section>

</body>
</html>
```